Manufacturing company needs new business card.

I need a unique Business Card that will truly stand out. Nothing too busy. Simple is good, right? Not looking for a standard design either. No cookie cutter layout. I am just looking for something interesting and a bit different. Does't have to completely off the wall crazy, just not your run of the mill business card. Clean and modern with a touch of industrial.

Target Market(s)

Air conditioning industry, Architects, builders.

Industry/Entity Type

Business

Contact Information for Business Card

Details to be included on card are:

Peter Vance
Managing Director

T: 1300 847 519
M: 0428 593 174
W: www.brenvaleworks.com.au
E: peter.vance@brenvaleworks.com.au
A: 58 Harwick Lane, Sydney NSW 2000

Font styles to use
Sans Serif

Colors
0355a3
848484
fbfbfb

Requirements
Must have
• Card design must be landscape.

```html
<!DOCTYPE html>
<html lang="en">
<head>
<meta charset="utf-8">
<title>Brenvale Works – Business Card</title>
<link rel="stylesheet" href="https://fonts.googleapis.com/css2?family=Quicksand:wght@400;500;600&display=swap">
<style>
  :root {
    --brand-blue: #0355a3;
    --card-blue: #1f3f93;
    --steel-grey: #848484;
    --card-white: #fbfbfb;
    --ink: #2b2b2b;
    --backdrop: #e9ecee;
  }
  * { box-sizing: border-box; margin: 0; padding: 0; }
  html, body {
    width: 1200px;
    height: 800px;
    overflow: hidden;
    background: var(--backdrop);
    font-family: "Quicksand", sans-serif;
  }
  .canvas {
    position: relative;
    width: 1200px;
    height: 800px;
    display: flex;
    align-items: center;
    justify-content: center;
    gap: 60px;
  }
  .card {
    position: relative;
    width: 520px;
    height: 300px;
    background: var(--card-white);
    box-shadow: 0 2px 10px rgba(0, 0, 0, 0.08);
    overflow: hidden;
  }
  .card__top-band {
    position: absolute;
    top: 0; left: 0; right: 0;
    height: 20px;
    background: var(--card-blue);
  }

  /* Front */
  .card-front__brand {
    position: absolute;
    top: 50%;
    left: 50%;
    transform: translate(-50%, -40%);
    display: flex;
    align-items: center;
    gap: 16px;
    white-space: nowrap;
  }
  .brand__square {
    width: 40px;
    height: 40px;
    background: var(--card-blue);
  }
  .brand__name {
    font-size: 36px;
    font-weight: 600;
    color: var(--card-blue);
    letter-spacing: 0.01em;
  }

  /* Back */
  .card-back__identity {
    position: absolute;
    top: 46px;
    right: 34px;
    text-align: right;
  }
  .identity__name {
    font-size: 30px;
    font-weight: 400;
    color: var(--card-blue);
    letter-spacing: 0.02em;
    line-height: 1.1;
  }
  .identity__title {
    font-size: 13px;
    font-weight: 500;
    color: var(--ink);
    margin-top: 4px;
    margin-right: 34px;
  }
  .card-back__icon-strip {
    position: absolute;
    left: 0;
    bottom: 0;
    width: 88px;
    height: 165px;
    background: var(--card-blue);
    display: flex;
    flex-direction: column;
    align-items: center;
    justify-content: space-around;
    padding: 16px 0 18px 14px;
  }
  .icon { width: 22px; height: 22px; }
  .card-back__contacts {
    position: absolute;
    left: 108px;
    bottom: 0;
    height: 165px;
    padding: 16px 0 18px;
    display: flex;
    flex-direction: column;
    justify-content: space-around;
    font-size: 13px;
    font-weight: 500;
    color: var(--ink);
    line-height: 1.35;
  }
</style>
</head>
<body>
<main class="canvas">

  <section class="card card-front" aria-label="Business card front">
    <div class="card__top-band"></div>
    <div class="card-front__brand">
      <span class="brand__square"></span>
      <span class="brand__name">Brenvale Works</span>
    </div>
  </section>

  <section class="card card-back" aria-label="Business card back">
    <div class="card__top-band"></div>

    <div class="card-back__identity">
      <h1 class="identity__name">PETER VANCE</h1>
      <p class="identity__title">Managing Director</p>
    </div>

    <div class="card-back__icon-strip" aria-hidden="true">
      <svg class="icon" viewBox="0 0 24 24" fill="none" stroke="#fff" stroke-width="1.2">
        <rect x="7" y="2.5" width="10" height="19" rx="1.5"/>
        <line x1="7" y1="5.5" x2="17" y2="5.5"/>
        <line x1="7" y1="18" x2="17" y2="18"/>
      </svg>
      <svg class="icon" viewBox="0 0 24 24" fill="none" stroke="#fff" stroke-width="1.2">
        <rect x="3" y="6" width="18" height="12"/>
        <polyline points="3,6 12,13 21,6"/>
      </svg>
      <svg class="icon" viewBox="0 0 24 24" fill="none" stroke="#fff" stroke-width="1.2">
        <rect x="3" y="5" width="18" height="12"/>
        <line x1="12" y1="17" x2="12" y2="20"/>
        <line x1="8" y1="20" x2="16" y2="20"/>
      </svg>
      <svg class="icon" viewBox="0 0 24 24" fill="none" stroke="#fff" stroke-width="1.2">
        <path d="M12 21s-6-6.2-6-11a6 6 0 0 1 12 0c0 4.8-6 11-6 11z"/>
        <circle cx="12" cy="10" r="2.2"/>
      </svg>
    </div>

    <address class="card-back__contacts" style="font-style: normal;">
      <span>1300 847 519<br>0428 593 174</span>
      <span>peter.vance@brenvaleworks.com.au</span>
      <span>www.brenvaleworks.com.au</span>
      <span>58 Harwick Lane, Sydney NSW 2000</span>
    </address>
  </section>

</main>
</body>
</html>
```